Diabetes Education Flyer Design Project

We need a 8.5" X 11" flyer design for a retail pharmacy located in Queens, NYC to promote our new program of "Free Diabetes Education". This flyer will be distributed to doctors offices and to places where people congregate. The flyer should create a fear to the audience about diabetes and an urgency to come or call the pharmacy to get more information on the "Free Diabetes Education". The target audience is 40+ years old with national background of West Indies and India. They are mostly blue color worker with a highschool or less education

Target Market(s)

People with diabetes aging 40+, from West Indies and India, low literacy level

Industry/Entity Type

Education

Requirements
Must have
• Must have graphics and colors to attract the targetted age/race/literacy. Must have graphics and colors to create fear at the begining and hope at the end.
Nice to have
• Fonts to support the theme

```html
<!DOCTYPE html>
<html lang="en">
<head>
<meta charset="utf-8">
<title>Free Diabetes Education Flyer</title>
<link rel="stylesheet" href="https://fonts.googleapis.com/css2?family=Fredoka:wght@600;700&family=Arimo:wght@400;700&display=swap">
<style>
  :root {
    --flyer-orange: #F7941D;
    --ink: #231F20;
    --paper: #FFFFFF;
    --brand-red: #E8202A;
  }
  html, body {
    margin: 0;
    padding: 0;
    overflow: hidden;
    background: var(--paper);
  }
  .flyer {
    width: 849px;
    height: 1200px;
    display: block;
  }
  .flyer-bg { fill: var(--flyer-orange); }
  .headline { font-family: "Fredoka", "Arial Rounded MT Bold", sans-serif; font-weight: 700; fill: var(--ink); }
  .question { font-family: "Fredoka", "Arial Rounded MT Bold", sans-serif; font-weight: 700; fill: var(--paper); }
  .footnote, .annual-note, .address { font-family: "Arimo", Arial, sans-serif; font-weight: 400; fill: var(--ink); }
  .footnote { font-size: 12.5px; }
  .annual-note { font-size: 14px; }
  .address { font-size: 19px; }
  .slogan-box, .slogan-rule, .slogan-ring { fill: none; stroke: var(--ink); stroke-width: 2; }
  .slogan-text { font-family: "Fredoka", "Arial Rounded MT Bold", sans-serif; font-weight: 600; fill: var(--ink); }
  .phone { font-family: "Fredoka", "Arial Rounded MT Bold", sans-serif; font-weight: 600; fill: var(--ink); font-size: 56px; }
  .brand-name { font-family: "Fredoka", "Arial Rounded MT Bold", sans-serif; font-weight: 600; fill: var(--brand-red); font-size: 38px; }
</style>
</head>
<body>
<svg class="flyer" viewBox="0 0 849 1200" xmlns="http://www.w3.org/2000/svg" aria-label="Free diabetes education flyer">
  <rect class="flyer-bg" x="0" y="0" width="849" height="1200"/>

  <!-- Fear headline -->
  <g class="stat-block">
    <text class="headline" x="62" y="114" font-size="88" textLength="396" lengthAdjust="spacingAndGlyphs">DIABETES</text>
    <text class="headline" x="60" y="229" font-size="138" textLength="314" lengthAdjust="spacingAndGlyphs">KILLS</text>
    <text class="headline" x="62" y="312" font-size="86" textLength="432" lengthAdjust="spacingAndGlyphs">3,4Million</text>
    <text class="headline" x="500" y="262" font-size="30">*</text>
    <text class="annual-note" x="508" y="326">annualy</text>
  </g>

  <g class="source-note">
    <text class="footnote" x="516" y="200">* According to World Health Orga-</text>
    <text class="footnote" x="516" y="217">nization in 2004, an estimated 3.4</text>
    <text class="footnote" x="516" y="234">million people died worldwide from</text>
    <text class="footnote" x="516" y="251">consequences of high blood sugar.</text>
    <text class="footnote" x="516" y="268">Fact Sheet No. 312 (August, 2011)</text>
  </g>

  <!-- Question -->
  <g class="question-block">
    <text class="question" x="40" y="604" font-size="206" textLength="772" lengthAdjust="spacingAndGlyphs">ARE U</text>
    <text class="question" x="48" y="830" font-size="262" textLength="760" lengthAdjust="spacingAndGlyphs">NEXT?</text>
  </g>

  <!-- Hope slogan -->
  <g class="slogan">
    <rect class="slogan-box" x="18" y="886" width="813" height="76"/>
    <line class="slogan-rule" x1="240" y1="924" x2="520" y2="924"/>
    <text class="slogan-text" x="232" y="919" font-size="34" text-anchor="end">LIVE</text>
    <text class="slogan-text" x="232" y="951" font-size="34" text-anchor="end">LONGER</text>
    <circle class="slogan-ring" cx="275" cy="924" r="30" fill="var(--flyer-orange)" style="fill:var(--flyer-orange)"/>
    <text class="slogan-text" x="275" y="935" font-size="32" text-anchor="middle">by</text>
    <text class="slogan-text" x="318" y="917" font-size="33">EDUCATING</text>
    <text class="slogan-text" x="318" y="949" font-size="31">yourself</text>
    <circle class="slogan-ring" cx="544" cy="924" r="28" style="fill:var(--flyer-orange)"/>
    <text class="slogan-text" x="544" y="934" font-size="28" text-anchor="middle">it's</text>
    <text class="headline" x="580" y="950" font-size="84" textLength="232" lengthAdjust="spacingAndGlyphs">FREE</text>
  </g>

  <!-- Contact -->
  <g class="contact">
    <text class="phone" x="364" y="1014" textLength="400" lengthAdjust="spacingAndGlyphs">(718)555.0142</text>
    <text class="brand-name" x="414" y="1072">Harbor Pharmacy</text>
    <text class="address" x="419" y="1118">88-20 Maple Ave.,</text>
    <text class="address" x="419" y="1142">Fairview, NY 11400</text>
  </g>
</svg>
</body>
</html>
```